Web Design Project

This web site is to be designed for a popular Cambodian singer, Pich Leakena. Web site name "Pich Leakena".

The purpose is to keep her fans update with the latest of her entertainment career and invite them to help raising fund for Mekong Little Hands Fund.

In addition to other normal pages such as HOME, ABOUT... This web site must be:
1. able to link to Dropshipers and add Products
2. able to donate (accept Major Credit Cards or CoinLark)
3. able to purchase products (accept Major Credit Cards or CoinLark)
4. able to video live chat with Pich Leakena
5. able to book appointment on her calendar

Here is a sample of the web site:
http://dorvel22.sitebarn.example/pich-lea-kena

Please call me if you need any clarification at 1-555-284-1937 or leave your number for me to call you back.

Thank you

Vuthy

Target Market(s)

Cambodian living abroad

Industry/Entity Type

Entertainment

Requirements
Must have
• 1. able to link to Dropshipers and add Products
2. able to Donate (accept Major Credit Cards or CoinLark)

```html
<!DOCTYPE html>
<html lang="en">
<head>
<meta charset="utf-8">
<title>Pich Leakena</title>
<link href="https://fonts.googleapis.com/css2?family=Fira+Sans+Extra+Condensed:ital,wght@0,400;0,500;1,400&family=Open+Sans:wght@400;600;700&family=Arimo:ital,wght@0,400;0,700;1,400&display=swap" rel="stylesheet">
<style>
:root{
  --bg:#130f12;
  --bg-deep:#0b0a0b;
  --header:#1c1226;
  --purple:#3a1f50;
  --orange:#f08a2c;
  --btn:#e06a10;
  --text:#c9c4c6;
  --muted:#a9a3a6;
  --white:#ffffff;
  --rule:#3a3336;
  --strip:#4a4b50;
}
*{margin:0;padding:0;box-sizing:border-box}
html,body{width:934px;height:1200px;overflow:hidden;background:var(--bg)}
.page{position:relative;width:934px;height:1200px;background:linear-gradient(180deg,#2a1738 0,#1a1020 420px,#1c1114 600px,var(--bg) 900px);font-family:"Arimo",sans-serif;color:var(--text)}
.abs{position:absolute}
.header{left:0;top:0;width:934px;height:66px;background:radial-gradient(ellipse at 300px 30px,#4a2a66 0,var(--header) 60%,#120e1c 100%);border-bottom:1px solid #4a4252}
.logo{left:85px;top:28px;font-family:"Open Sans",sans-serif;font-weight:700;font-size:23px;letter-spacing:.5px;color:#e6e2e6}
.nav{top:35px;font-family:"Arimo",sans-serif;font-size:11px;color:var(--white)}
.nav.active{background:#bdbdc2;color:#222;border-radius:10px;padding:3px 12px;top:32px}
.hero-frame{left:59px;top:94px;width:818px;height:390px;background:linear-gradient(180deg,#3a3a3e,#161618 40px);padding:8px}
.hero-video{left:94px;top:124px;width:748px;height:358px;border:1px solid #444;background:radial-gradient(ellipse at 470px 200px,#3a2630 0,#16101a 45%,#050406 80%)}
.strip{left:0;top:482px;width:934px;height:92px;background:linear-gradient(180deg,#5a5b60,#34353a 60%,#2a2b2f);box-shadow:0 6px 14px #000}
.strip-notch{left:458px;top:470px}
.thumb{top:495px;width:131px;height:66px;border:1px solid #9a9aa0}
.arrow{top:516px;width:34px;height:26px;background:linear-gradient(#8b8c91,#5c5d62);border-radius:13px}
.col-h{font-family:"Fira Sans Extra Condensed",sans-serif;font-style:italic;font-size:25px;color:var(--white)}
.rule{height:1px;background:var(--rule)}
.photo{width:98px;height:98px;border:2px solid #e07a3a;border-radius:3px}
.sub-h{font-family:"Fira Sans Extra Condensed",sans-serif;font-size:20px;color:var(--orange)}
.body{font-size:10px;line-height:17px;color:var(--muted);letter-spacing:.2px}
.tick{font-family:"Open Sans",sans-serif;font-size:13px;line-height:17px;color:var(--text)}
.tick b{color:var(--white)}
.quote{font-style:italic;font-size:10.5px;line-height:17px;color:var(--muted)}
.field{width:168px;height:19px;background:#fff;border:1px solid #999;font-size:9px;color:#333;padding:3px 7px}
.btn{width:74px;height:19px;background:var(--btn);color:#fff;font-family:"Open Sans",sans-serif;font-weight:700;font-size:10px;text-align:center;line-height:19px}
.cond{font-family:"Fira Sans Extra Condensed",sans-serif}
.footer{left:0;top:1070px;width:934px;height:72px;background:#1a1a1c;border-top:1px solid #3a3a3e;border-bottom:1px solid #3a3a3e}
.social{top:1089px;width:40px;height:36px;border-radius:4px;background:linear-gradient(#6a6a70,#3a3a40);color:#fff;font-family:"Open Sans",sans-serif;font-weight:700;font-size:8px;text-align:center;line-height:36px}
.bottom{left:0;top:1142px;width:934px;height:58px;background:var(--bg-deep)}
.flink{top:1153px;font-family:"Open Sans",sans-serif;font-weight:600;font-size:11px;color:#bdbdbd}
</style>
</head>
<body>
<div class="page">
  <header class="abs header"></header>
  <div class="abs logo">PICH LEAKENA</div>
  <span class="abs nav active" style="left:420px">HOME</span>
  <span class="abs nav" style="left:535px">ABOUT</span>
  <span class="abs nav" style="left:627px">VIDEOS</span>
  <span class="abs nav" style="left:726px">STORE</span>
  <span class="abs nav" style="left:820px">LIVE CHAT</span>

  <div class="abs hero-frame"></div>
  <div class="abs hero-video" role="img" aria-label="Featured concert video still of the singer on stage"></div>
  <svg class="abs" style="left:436px;top:285px" width="64" height="70" viewBox="0 0 64 70">
    <path d="M12 40a20 20 0 0 1 32-22" fill="none" stroke="#eee" stroke-width="7"/>
    <path d="M52 30a20 20 0 0 1-32 22" fill="none" stroke="#eee" stroke-width="7"/>
    <path d="M38 8l12 10-14 6z" fill="#eee"/><path d="M26 62l-12-10 14-6z" fill="#eee"/>
  </svg>

  <div class="abs strip"></div>
  <svg class="abs strip-notch" width="18" height="13"><path d="M0 13L9 0 18 13z" fill="#5a5b60"/></svg>
  <div class="abs arrow" style="left:59px"><svg width="34" height="26"><path d="M17 8l-5 5 5 5" fill="none" stroke="#e07a3a" stroke-width="2.5"/></svg></div>
  <div class="abs thumb" style="left:95px;background:linear-gradient(135deg,#3a2a55,#6a4a30)" role="img" aria-label="Video thumbnail: singer performing on stage"></div>
  <div class="abs thumb" style="left:249px;background:linear-gradient(135deg,#2a1a1a,#8a3a2a)" role="img" aria-label="Video thumbnail: singer with microphone"></div>
  <div class="abs thumb" style="left:403px;background:linear-gradient(135deg,#3a1a20,#6a3a40)" role="img" aria-label="Video thumbnail: singer smiling on stage"></div>
  <div class="abs thumb" style="left:557px;background:linear-gradient(135deg,#1a1a20,#4a4a50)" role="img" aria-label="Video thumbnail: duet performance"></div>
  <svg class="abs" style="left:615px;top:521px" width="14" height="14"><path d="M7 1v12M1 7h12" stroke="#fff" stroke-width="2"/></svg>
  <div class="abs thumb" style="left:709px;background:linear-gradient(135deg,#4a2a4a,#8a4a6a)" role="img" aria-label="Video thumbnail: singer with parasol"></div>
  <div class="abs arrow" style="left:842px"><svg width="34" height="26"><path d="M15 8l5 5-5 5" fill="none" stroke="#333" stroke-width="2.5"/></svg></div>

  <div class="abs col-h" style="left:63px;top:606px">Store</div>
  <div class="abs rule" style="left:63px;top:642px;width:535px"></div>
  <div class="abs photo" style="left:63px;top:651px;background:linear-gradient(#f2f2f2,#d8d0cc)" role="img" aria-label="Portrait of the singer for the store"></div>
  <div class="abs sub-h" style="left:177px;top:652px">Purchase Products</div>
  <p class="abs body" style="left:177px;top:683px;width:421px">Lorem Ipsum is simply dummy text of the printing and typesetting industry. Lorem Ipsum has been the industry's standard dummy text ever since the 1500s, when an unknown printer took a galley of type and scrambled it to make a type specimen book. It has survived not only five centuries, but also the leap into electronic typesetting.</p>

  <div class="abs col-h" style="left:63px;top:756px">Purpose</div>
  <div class="abs rule" style="left:63px;top:791px;width:535px"></div>
  <div class="abs photo" style="left:63px;top:802px;background:linear-gradient(#dfe4ea,#9aa0aa)" role="img" aria-label="Portrait of the singer for the purpose section"></div>
  <div class="abs sub-h" style="left:177px;top:800px">Why This Site?</div>
  <p class="abs tick" style="left:177px;top:829px;width:421px">✔ I would like to keep you all update with the latest of my entertainment career.</p>
  <p class="abs tick" style="left:177px;top:871px;width:421px">✔ Another purpose of this site is to help raising fund for <b>Mekong Little Hands Fund.</b></p>

  <div class="abs col-h" style="left:63px;top:906px">Live Chat</div>
  <div class="abs rule" style="left:63px;top:941px;width:535px"></div>
  <div class="abs photo" style="left:63px;top:951px;background:linear-gradient(#6a6a6a,#1a1a1a)" role="img" aria-label="Portrait of the singer for live chat"></div>
  <div class="abs sub-h" style="left:177px;top:951px">You Can Talk To Pich Leakena</div>
  <p class="abs body" style="left:177px;top:983px;width:421px">Lorem Ipsum is simply dummy text of the printing and typesetting industry. Lorem Ipsum has been the industry's standard dummy text ever since the 1500s, when an unknown printer took a galley of type and scrambled it to make a type specimen book. It has survived not only five centuries ........ <i style="color:var(--orange)">Click Here</i></p>

  <div class="abs col-h" style="left:623px;top:606px">About Me</div>
  <div class="abs rule" style="left:623px;top:642px;width:255px"></div>
  <p class="abs quote" style="left:623px;top:655px;width:255px">"Lorem ipsum dolor sit amet, consectetur adipisicing elit, sed do eiusmod tempor incididunt ut labore et dolore magna aliqua. Ut enim ad minim veniam, quis nostrud exercitation ullamco laboris nisi ut aliquip ex ea commodo consequat. Duis aute irure dolor in reprehenderit in voluptate velit esse cillum dolore eu fugiat nulla pariatur"</p>

  <div class="abs col-h" style="left:623px;top:786px">Donate</div>
  <div class="abs rule" style="left:623px;top:822px;width:255px"></div>
  <svg class="abs" style="left:621px;top:840px" width="46" height="32"><circle cx="16" cy="10" r="7" fill="#8a8a8a"/><circle cx="30" cy="10" r="7" fill="#9a9a9a"/><path d="M2 30q0-14 14-14t14 14zM18 30q0-14 14-14t12 14z" fill="#8a8a8a"/></svg>
  <div class="abs cond" style="left:674px;top:836px;font-size:15px;color:#d8d8d8">Help us raise funds for</div>
  <div class="abs cond" style="left:674px;top:853px;font-size:19px;font-weight:500;color:#e0e0e0">Mekong Little Hands Fund</div>
  <div class="abs field" style="left:624px;top:889px">Email Address</div>
  <div class="abs btn" style="left:803px;top:889px">DONATE</div>

  <div class="abs col-h" style="left:626px;top:924px">Drop Shippers / Add Products</div>
  <p class="abs cond" style="left:624px;top:965px;width:258px;font-size:13px;line-height:15px;color:#d0d0d0">Lorem ipsum dolor sit amet, consectetur adipisicing elit, sed do eiusmod tempor incididunt ut labore et dolore magna aliqua.</p>
  <div class="abs field" style="left:624px;top:1026px">Email Address</div>
  <div class="abs btn" style="left:803px;top:1026px">GO</div>

  <footer class="abs footer"></footer>
  <div class="abs" style="left:68px;top:1097px;font-family:'Open Sans',sans-serif;font-size:15px;color:#e0e0e0">Chirpline</div>
  <p class="abs" style="left:160px;top:1088px;width:400px;font-size:10px;line-height:18px;color:#e0e0e0">Lorem ipsum dolor sit amet, consectetur adipisicing elit, sed do eiusmod tempor incididunt ut labore et dolore magna aliqua. Ut enim ad minim veniam.</p>
  <div class="abs" style="left:616px;top:1084px;width:1px;height:44px;background:#444"></div>
  <div class="abs social" style="left:657px">Friend</div>
  <div class="abs social" style="left:713px">Diglet</div>
  <div class="abs social" style="left:769px">Feed</div>
  <div class="abs social" style="left:825px">Snapreel</div>

  <div class="abs bottom"></div>
  <span class="abs flink" style="left:267px">HOME</span>
  <span class="abs flink" style="left:323px">|</span>
  <span class="abs flink" style="left:354px">ABOUT</span>
  <span class="abs flink" style="left:423px">|</span>
  <span class="abs flink" style="left:453px">VIDEO</span>
  <span class="abs flink" style="left:510px">|</span>
  <span class="abs flink" style="left:538px">STORE</span>
  <span class="abs flink" style="left:593px">|</span>
  <span class="abs flink" style="left:620px">LIVE CHAT</span>
  <div class="abs" style="left:0;top:1175px;width:934px;text-align:center;font-family:'Open Sans',sans-serif;font-weight:600;font-size:10px;color:#9a9a9a">Copyright © Pich Leakena</div>
</div>
</body>
</html>
```